Ice Cream Cup Design

We need a packaging design for ice cream cups.
We're a London based company called Villa Rosa Dolci and are producers of fresh Italian Artisan Gelato our website is www.villarosadolci.co.uk

We're looking to invest in a cup filling machine to fill 100ml and 500ml cups of gelato.
The 500ml cup will be the same shape and height as the Nordvik Freeze tub with a matching lid design.
The 100ml cup will be of the same shape and height of the Nordvik Freeze Single Serve cup with a matching lid design and includes a spoon inside.

We're looking for edgy clean designs that give an impression of quality and draw attention to the product if it sat on a product shelf. Inspired by packaging such as Ko, Pemberly and Harrowfield we're keen on a black themed packaging with a striking contrast of simple colour and a simple ice cream or gelato image that shows more than one flavour.
This particular design is not boasting any particular flavour, its a uniform design across our whole range of flavours.

Our company logo may be too fussy for this packaging so we would like to include our company ice cream logo and a way to include our company name but still look edgy for example - just like Pemberly Tea - our ice cream logo big G underneath, then 'VILLA ROSA DOLCI' underneath, and below that 'ARTISAN ITALIAN GELATO'. Or anything that inspires and looks good, will draw attention and looks sexy and indulgent and gives an impression of luxury product.

Please check attached document for cup shape and dimensions.

Reason: Christmas and New Year Holiday period resulted in less time for feedback opportunity and new designs to be posted.

Target Market(s)

Target market between 20-40 years old, consumers of quality desserts all year round.

Industry/Entity Type

It Company

Requirements
Must have
• Our Ice Cream Logo
Our name (doesn't need to necessarily have it in our font, can be in bold lettering)
Nice to have
• Limited writing and fuss.
Ideal to have simple clean designs
Should not have
• Eccentric colours and fun childlike images.

```html
<!DOCTYPE html>
<html lang="en">
<head>
<meta charset="utf-8">
<title>Villa Rosa Dolci – 500ml Gelato Label</title>
<link rel="stylesheet" href="https://fonts.googleapis.com/css2?family=Montserrat:wght@300;400&display=swap">
<style>
  :root {
    --ink: #000000;
    --glow-core: #7a0f4a;
    --glow-mid: #3e0626;
    --glow-edge: #120009;
    --magenta-line: #d0177a;
    --cream: #ffffff;
    --placeholder-a: rgba(255, 255, 255, 0.16);
    --placeholder-b: rgba(255, 255, 255, 0.04);
  }

  html, body {
    margin: 0;
    padding: 0;
    width: 1200px;
    height: 1200px;
    overflow: hidden;
    background: var(--ink);
  }

  .label {
    position: relative;
    width: 1200px;
    height: 1200px;
    overflow: hidden;
    font-family: "Montserrat", sans-serif;
    color: var(--cream);
    background:
      radial-gradient(ellipse 520px 560px at 600px 600px,
        var(--glow-core) 0%,
        var(--glow-mid) 45%,
        var(--glow-edge) 75%,
        var(--ink) 100%);
  }

  .label__cone-mark {
    position: absolute;
    left: 440px;
    top: 220px;
    width: 330px;
    height: 450px;
    border-radius: 48% 48% 30% 30% / 40% 40% 60% 60%;
    background: radial-gradient(ellipse at 50% 35%, var(--placeholder-a), var(--placeholder-b) 70%, transparent 100%);
  }

  .label__brand-name {
    position: absolute;
    left: 0;
    width: 1200px;
    top: 710px;
    margin: 0;
    text-align: center;
    font-weight: 300;
    font-size: 92px;
    line-height: 1;
    letter-spacing: 1px;
  }

  .label__volume {
    position: absolute;
    left: 0;
    width: 1200px;
    top: 910px;
    margin: 0;
    text-align: center;
    font-weight: 400;
    font-size: 38px;
    line-height: 1;
  }

  .label__wave {
    position: absolute;
    left: 0;
    top: 975px;
    width: 1200px;
    height: 50px;
  }

  .label__tagline {
    position: absolute;
    left: 0;
    width: 1200px;
    top: 1090px;
    margin: 0;
    text-align: center;
    font-weight: 400;
    font-size: 40px;
    line-height: 1;
    letter-spacing: 1px;
  }
</style>
</head>
<body>
  <main class="label">
    <div class="label__cone-mark" role="img" aria-label="Company ice cream logo: line-drawn gelato cone with scooped top and waffle cone"></div>

    <h1 class="label__brand-name">Villa Rosa Dolci</h1>

    <p class="label__volume">500ml</p>

    <svg class="label__wave" viewBox="0 0 1200 50" aria-hidden="true">
      <path d="M0 25 C 200 30, 400 20, 600 26 S 1000 32, 1200 22" fill="none" stroke="var(--magenta-line)" stroke-width="2"/>
    </svg>

    <p class="label__tagline">ARTISAN ITALIAN GELATO</p>
  </main>
</body>
</html>
```